Crestmoor Business Cards

I need a business card designed with the following information.

Company Name: Crestmoor Wealth Management
Name: BriAnne Tolvey
Title: Executive Assistant
Cell: (555) 302-7164
Direct Line: (555) 917-5082
Email: brianne@crestmoorwm.example
Address: 20537 W. Harwell PKWY Ste. B
Fernhollow, WR 77512

I have attached the logo.
I would like it in navy blue and silver.
Thanks.

```html
<!DOCTYPE html>
<html lang="en">
<head>
<meta charset="utf-8">
<title>Crestmoor Wealth Management – Business Card</title>
<link href="https://fonts.googleapis.com/css2?family=Lato:wght@400;700&display=swap" rel="stylesheet">
<style>
  :root {
    --backdrop: #2b2b2d;
    --navy: #13284d;
    --navy-text: #1b2d55;
    --silver: #d9dbe0;
    --paper: #f1f1f1;
    --ink-grey: #6f7177;
    --rule: #1b2d55;
  }
  * { box-sizing: border-box; margin: 0; padding: 0; }
  html, body {
    width: 1200px; height: 800px; overflow: hidden;
    background: var(--backdrop);
    font-family: "Lato", sans-serif;
  }
  .canvas {
    width: 1200px; height: 800px;
    display: flex; flex-direction: column;
    align-items: center; justify-content: center; gap: 36px;
  }
  .card {
    width: 580px; height: 331px; position: relative;
    box-shadow: 0 10px 24px rgba(0,0,0,.45);
  }
  /* Front */
  .card-front {
    background: var(--navy);
    display: flex; flex-direction: column; align-items: center; justify-content: center;
    color: var(--silver);
  }
  .front-brand {
    display: flex; align-items: center; gap: 14px;
    font-weight: 700; font-size: 40px; letter-spacing: 6px; text-transform: uppercase;
  }
  .brand-mark { width: 22px; height: 22px; background: var(--silver); flex: none; }
  .front-web {
    position: absolute; bottom: 46px; left: 0; right: 0; text-align: center;
    font-size: 13px; letter-spacing: 4px;
  }
  /* Back */
  .card-back {
    background: var(--paper);
    display: grid; grid-template-columns: 46% 1px 1fr; align-items: center;
  }
  .back-brand {
    display: flex; flex-direction: column; align-items: center; gap: 8px;
    padding: 0 18px;
    color: var(--navy-text); font-weight: 400;
  }
  .back-brand-name {
    display: flex; align-items: center; gap: 9px;
    font-size: 22px; letter-spacing: 5px; text-transform: uppercase; white-space: nowrap;
  }
  .back-brand-name .brand-mark { width: 13px; height: 13px; background: var(--navy-text); }
  .back-brand-tag { font-size: 10px; letter-spacing: 3px; text-transform: uppercase; }
  .divider { width: 1px; height: 150px; background: var(--rule); }
  .contact { padding-left: 34px; color: var(--ink-grey); font-size: 13px; line-height: 1.35; }
  .contact-name { color: var(--navy-text); font-weight: 700; font-size: 17px; }
  .contact-title { margin-bottom: 10px; }
  .contact-address { margin-bottom: 8px; }
  .contact-list { list-style: none; }
  .contact-list li { display: flex; align-items: center; gap: 7px; white-space: nowrap; }
  .contact-list svg { width: 11px; height: 11px; fill: var(--navy-text); flex: none; }
</style>
</head>
<body>
<main class="canvas">
  <section class="card card-front">
    <div class="front-brand"><span class="brand-mark"></span>Crestmoor</div>
    <p class="front-web">www.crestmoorwm.example</p>
  </section>

  <section class="card card-back">
    <div class="back-brand">
      <div class="back-brand-name"><span class="brand-mark"></span>Crestmoor</div>
      <div class="back-brand-tag">Wealth Management</div>
    </div>
    <div class="divider"></div>
    <div class="contact">
      <p class="contact-name">BriAnne Tolvey</p>
      <p class="contact-title">Executive Assistant</p>
      <p class="contact-address">20537 W. Harwell PKWY Ste. B<br>Fernhollow, WR 77512</p>
      <ul class="contact-list">
        <li><svg viewBox="0 0 24 24"><path d="M6.6 10.8a15 15 0 0 0 6.6 6.6l2.2-2.2a1 1 0 0 1 1-.25 11.4 11.4 0 0 0 3.6.57 1 1 0 0 1 1 1V20a1 1 0 0 1-1 1A17 17 0 0 1 3 4a1 1 0 0 1 1-1h3.5a1 1 0 0 1 1 1c0 1.25.2 2.45.57 3.57a1 1 0 0 1-.25 1z"/></svg>(555) 302-7164</li>
        <li><svg viewBox="0 0 24 24"><path d="M7 1h10a2 2 0 0 1 2 2v18a2 2 0 0 1-2 2H7a2 2 0 0 1-2-2V3a2 2 0 0 1 2-2zm0 3v14h10V4zm5 15.5a1 1 0 1 0 0 2 1 1 0 0 0 0-2z"/></svg>(555) 917-5082</li>
        <li><svg viewBox="0 0 24 24"><path d="M2 5h20v14H2zm2 2v.5l8 5 8-5V7zm0 2.8V17h16V9.8l-8 5z"/></svg>brianne@crestmoorwm.example</li>
        <li><svg viewBox="0 0 24 24"><path d="M12 2a10 10 0 1 0 0 20 10 10 0 0 0 0-20zm6.9 6h-3a15 15 0 0 0-1.3-3.9A8 8 0 0 1 18.9 8zM12 4c.9 1.2 1.6 2.5 2 4h-4c.4-1.5 1.1-2.8 2-4zM4.3 14a8 8 0 0 1 0-4h3.4a16 16 0 0 0 0 4zm.8 2h3a15 15 0 0 0 1.3 3.9A8 8 0 0 1 5.1 16zM8 8H5.1a8 8 0 0 1 4.3-3.9A15 15 0 0 0 8 8zm4 12c-.9-1.2-1.6-2.5-2-4h4c-.4 1.5-1.1 2.8-2 4zm2.3-6H9.7a14 14 0 0 1 0-4h4.6a14 14 0 0 1 0 4zm.3 5.9A15 15 0 0 0 15.9 16h3a8 8 0 0 1-4.3 3.9zM16.3 14a16 16 0 0 0 0-4h3.4a8 8 0 0 1 0 4z"/></svg>www.crestmoorwm.example</li>
      </ul>
    </div>
  </section>
</main>
</body>
</html>
```